Set of 6 Icons and buttons required

We have written a windows based app which gives clients access to reports etc.

We are a multichannel epos company

We require 6 buttons and icons along with a suggested font to use and a background for the form.

I have attatched a mock up of what we require from the chosen designer.

The buttons are as follows :

Stockcard ( This is a program which customers can enter stock and check stock levels etc )

Reports ( as the title says )

Stock ( This for making adjustments )

Goods ( this is for booking goods in )

Settings ( As title says )

Help ( As title says )

Dimensions
---------------

The form : 296x268
Buttons : 218x36
Icons on button : 32x32
Text size : Size 10

If you look at the attatched document this is something I put together just to show what we are looking once we put all the components together

Our website is q-ledgora.co.uk

Target Market(s)

B2B

Industry/Entity Type

It Company

```html
<!DOCTYPE html>
<html lang="en">
<head>
<meta charset="utf-8">
<title>q-ledgora — launcher buttons</title>
<link rel="stylesheet" href="https://fonts.googleapis.com/css2?family=Roboto+Condensed:wght@400&display=swap">
<style>
  :root {
    --canvas: #ffffff;
    --navy-btn: #0e5fa9;
    --sky-btn: #00aeef;
    --icon-well-grey: #e6e7e8;
    --icon-well-white: #ffffff;
    --icon-ink: #9d9fa2;
    --label: #ffffff;
    --titlebar-top: #e9eaec;
    --titlebar-bottom: #b9bbc0;
    --window-deep: #2c2466;
    --window-mid: #4a3478;
    --window-light: #6b4c8c;
  }
  * { box-sizing: border-box; margin: 0; padding: 0; }
  html, body { width: 1200px; height: 1193px; overflow: hidden; background: var(--canvas); }
  body { position: relative; font-family: "Roboto Condensed", "Arial Narrow", sans-serif; }

  .app-window { position: absolute; left: 295px; top: 177px; width: 610px; height: 550px; overflow: hidden;
    background: radial-gradient(ellipse 70% 60% at 62% 22%, var(--window-light) 0%, transparent 70%),
                linear-gradient(120deg, var(--window-deep) 0%, var(--window-mid) 55%, var(--window-light) 100%); }
  .titlebar { height: 33px; background: linear-gradient(var(--titlebar-top), var(--titlebar-bottom));
    display: flex; justify-content: flex-end; align-items: center; gap: 22px; padding-right: 22px; }
  .titlebar svg { width: 14px; height: 12px; }

  .brand-name { position: absolute; left: 0; top: 290px; width: 169px; text-align: center;
    color: #ffffff; font-size: 26px; line-height: 1; white-space: nowrap; }

  .window-menu { position: absolute; left: 169px; top: 76px; width: 406px; }

  .menu-btn { display: flex; align-items: stretch; }
  .menu-btn .icon-well { display: flex; align-items: center; justify-content: center; }
  .menu-btn .icon-well svg { color: var(--icon-ink); }
  .menu-btn .label { flex: 1; display: flex; align-items: center; color: var(--label); }
  .menu-btn.is-navy .label { background: var(--navy-btn); }
  .menu-btn.is-sky .label { background: var(--sky-btn); }
  .menu-btn.on-grey .icon-well { background: var(--icon-well-grey); }
  .menu-btn.on-white .icon-well { background: var(--icon-well-white); }

  .window-menu .menu-btn { height: 71.5px; }
  .window-menu .icon-well { width: 143px; }
  .window-menu .icon-well svg { width: 40px; height: 40px; }
  .window-menu .label { font-size: 34px; padding-left: 102px; }

  .button-set { position: absolute; top: 804px; display: flex; flex-direction: column; gap: 21px; }
  .button-set.left { left: 196px; }
  .button-set.right { left: 647px; }
  .button-set .menu-btn { width: 357px; height: 62px; }
  .button-set .menu-btn.on-white .icon-well { border: 1px solid #e3e4e5; border-right: none; }
  .button-set .icon-well { width: 126px; }
  .button-set .icon-well svg { width: 38px; height: 38px; }
  .button-set .label { font-size: 31px; justify-content: center; padding-left: 30px; }
</style>
</head>
<body>
<svg width="0" height="0" style="position:absolute" aria-hidden="true">
  <defs>
    <symbol id="icon-stockcard" viewBox="0 0 32 32">
      <rect x="9" y="3" width="14" height="6" fill="none" stroke="currentColor" stroke-width="2"/>
      <rect x="7" y="9" width="18" height="20" fill="currentColor"/>
      <g stroke="#ffffff" stroke-width="1.4"><line x1="7" y1="14" x2="25" y2="14"/><line x1="7" y1="19" x2="25" y2="19"/><line x1="7" y1="24" x2="25" y2="24"/></g>
    </symbol>
    <symbol id="icon-reports" viewBox="0 0 32 32">
      <rect x="6" y="5" width="18" height="24" rx="2" fill="currentColor"/>
      <rect x="11" y="3" width="8" height="4" rx="1" fill="currentColor"/>
      <g stroke="#ffffff" stroke-width="1.6"><line x1="9" y1="12" x2="21" y2="12"/><line x1="9" y1="16" x2="21" y2="16"/><line x1="9" y1="20" x2="21" y2="20"/><line x1="9" y1="24" x2="17" y2="24"/></g>
      <path d="M22 28 L28 16 L30 17 L24 29 Z" fill="currentColor"/>
    </symbol>
    <symbol id="icon-stock" viewBox="0 0 32 32">
      <rect x="7" y="4" width="18" height="25" rx="2" fill="currentColor"/>
      <g stroke="#ffffff" stroke-width="1.4"><line x1="7" y1="10" x2="25" y2="10"/><line x1="7" y1="15" x2="25" y2="15"/><line x1="7" y1="20" x2="25" y2="20"/><line x1="7" y1="25" x2="25" y2="25"/></g>
    </symbol>
    <symbol id="icon-goods" viewBox="0 0 32 32">
      <path d="M7 14 H25 V28 H7 Z" fill="currentColor"/>
      <path d="M7 14 L2 8 L12 6 L16 11 L20 6 L30 8 L25 14 Z" fill="currentColor" opacity=".75"/>
      <line x1="7" y1="19" x2="25" y2="19" stroke="#ffffff" stroke-width="1.4"/>
    </symbol>
    <symbol id="icon-setting" viewBox="0 0 32 32">
      <circle cx="12" cy="21" r="6" fill="none" stroke="currentColor" stroke-width="4" stroke-dasharray="2.4 1.6"/>
      <circle cx="12" cy="21" r="4.5" fill="none" stroke="currentColor" stroke-width="3"/>
      <circle cx="23" cy="10" r="4" fill="none" stroke="currentColor" stroke-width="3" stroke-dasharray="1.8 1.3"/>
      <circle cx="23" cy="10" r="3" fill="none" stroke="currentColor" stroke-width="2"/>
    </symbol>
    <symbol id="icon-help" viewBox="0 0 32 32">
      <circle cx="16" cy="16" r="11" fill="none" stroke="currentColor" stroke-width="6" stroke-dasharray="8.6 8.7" stroke-dashoffset="4.3"/>
      <circle cx="16" cy="16" r="13.5" fill="none" stroke="currentColor" stroke-width="1"/>
      <circle cx="16" cy="16" r="8" fill="none" stroke="currentColor" stroke-width="1"/>
    </symbol>
  </defs>
</svg>

<section class="app-window" aria-label="q-ledgora launcher window">
  <div class="titlebar">
    <svg viewBox="0 0 14 12"><rect x="1" y="6" width="12" height="4" fill="none" stroke="#6d6e71"/></svg>
    <svg viewBox="0 0 14 12"><rect x="1" y="1" width="12" height="10" fill="none" stroke="#6d6e71"/><rect x="4" y="4" width="6" height="4" fill="#6d6e71"/></svg>
    <svg viewBox="0 0 14 12"><rect x="1" y="1" width="12" height="10" fill="none" stroke="#6d6e71"/><path d="M4 3 L10 9 M10 3 L4 9" stroke="#6d6e71"/></svg>
  </div>

  <span class="brand-name">q-ledgora</span>

  <nav class="window-menu">
    <div class="menu-btn is-navy on-grey"><span class="icon-well"><svg><use href="#icon-stockcard"/></svg></span><span class="label">Stockcard</span></div>
    <div class="menu-btn is-sky on-white"><span class="icon-well"><svg><use href="#icon-reports"/></svg></span><span class="label">Reports</span></div>
    <div class="menu-btn is-navy on-grey"><span class="icon-well"><svg><use href="#icon-stock"/></svg></span><span class="label">Stock</span></div>
    <div class="menu-btn is-sky on-white"><span class="icon-well"><svg><use href="#icon-goods"/></svg></span><span class="label">Goods</span></div>
    <div class="menu-btn is-navy on-grey"><span class="icon-well"><svg><use href="#icon-setting"/></svg></span><span class="label">Setting</span></div>
    <div class="menu-btn is-sky on-white"><span class="icon-well"><svg><use href="#icon-help"/></svg></span><span class="label">Help</span></div>
  </nav>
</section>

<div class="button-set left">
  <div class="menu-btn is-navy on-grey"><span class="icon-well"><svg><use href="#icon-stockcard"/></svg></span><span class="label">Stockcard</span></div>
  <div class="menu-btn is-sky on-white"><span class="icon-well"><svg><use href="#icon-reports"/></svg></span><span class="label">Reports</span></div>
  <div class="menu-btn is-navy on-grey"><span class="icon-well"><svg><use href="#icon-stock"/></svg></span><span class="label">Stock</span></div>
</div>

<div class="button-set right">
  <div class="menu-btn is-sky on-white"><span class="icon-well"><svg><use href="#icon-goods"/></svg></span><span class="label">Goods</span></div>
  <div class="menu-btn is-navy on-grey"><span class="icon-well"><svg><use href="#icon-setting"/></svg></span><span class="label">Setting</span></div>
  <div class="menu-btn is-sky on-white"><span class="icon-well"><svg><use href="#icon-help"/></svg></span><span class="label">Help</span></div>
</div>
</body>
</html>
```